NetStar Trust Brochure -- tri-fold

I need a logo design and brochure layout for a new fund I've established to support girls who are interested in participating in volleyball, but lack the funds to pay full price. The brochure will be used to raise money for the fund. I've attached a description of the fund's goals and requirements for distribution to help describe what we do. Feel free to use as much or as little as you wish. I look forward to receiving your ideas!

LATE NOTE: I've seen many awesome submissions, but I want to acknowledge that the I realize if we use all the copy I provided, it will be suffocating to the reader. So, please feel free to design and include whatever text you think would be most compelling to a target contributor.

Target Market(s)

Parent donors to the fund

Industry/Entity Type

It Support

Logo Text

NetStar Trust

Font styles to use
Serif
Sans Serif

Colors
0255a3
ecf7fb

Requirements
Must have
• Contact: netstartrust@mailbox-example.net or Margaret Clevin at 5558471926
• Colors are navy and silver -- UPDATE this was tough to select from the color wheel below so I did my best, but navy and traditional silver are definite
• Donations are not tax deductible
Nice to have
• Our mission:
• * Provide financial support to pre-high school volleyball players who are committed to volleyball, but lack the financial support necessary to participate in the program to which they have been accepted.
• * Seek dedicated athletes who are willing to invest in their future participation in volleyball either through direct financial participation or volunteer opportunities or both to further their futures in volleyball.
• *Reward players who recognize that participation in volleyball is an opportunity as well as a commitment and are dedicated to adhering to the expectations of the team to which they are invited to join, and becoming a positive leader and contributor to the team.

```html
<!DOCTYPE html>
<html lang="en">
<head>
<meta charset="utf-8">
<title>NetStar Trust – Tri-fold Brochure</title>
<link href="https://fonts.googleapis.com/css2?family=Anton&family=Montserrat:wght@300;400&family=Roboto+Condensed:wght@400;700&family=Roboto:wght@400&display=swap" rel="stylesheet">
<style>
  :root {
    --stage: #d9d9d9;
    --panel: #f2f2f2;
    --navy: #0a5aa5;
    --blue: #1d6fc0;
    --blue-mid: #4c9de0;
    --blue-light: #9fd0f5;
    --ink: #1e1e1e;
    --ink-soft: #555;
    --white: #ffffff;
  }
  * { margin: 0; padding: 0; box-sizing: border-box; }
  html, body { width: 1200px; height: 888px; overflow: hidden; background: var(--stage); }
  .brochure {
    position: absolute; left: 45px; top: 64px;
    width: 1110px; height: 760px; overflow: hidden;
    background: var(--panel);
  }
  .brochure-art { position: absolute; inset: 0; }

  /* left panel */
  .info-copy {
    position: absolute; left: 28px; top: 320px; width: 318px;
    font-family: "Montserrat", sans-serif; font-size: 13.5px; line-height: 1.45;
    color: var(--ink); letter-spacing: 0.3px;
  }
  .info-copy p + p { margin-top: 16px; }

  /* middle panel */
  .payment-note {
    position: absolute; left: 370px; top: 222px; width: 370px; text-align: center;
    font-family: "Montserrat", sans-serif; font-weight: 300; font-size: 21px; color: var(--ink);
  }
  .payment-note .payee {
    display: block; color: var(--blue); font-weight: 400; font-size: 22px;
    text-decoration: underline; text-underline-offset: 3px; margin-top: 2px;
  }
  .contact-pill {
    position: absolute; left: 430px; top: 316px; width: 250px; height: 40px;
    border-radius: 20px; background: var(--blue); color: var(--white);
    font-family: "Roboto Condensed", sans-serif; font-weight: 700; font-size: 23px;
    letter-spacing: 1px; text-align: center; line-height: 40px;
  }
  .contact-card {
    position: absolute; left: 410px; top: 386px; width: 320px;
    font-family: "Roboto", sans-serif; color: var(--ink);
  }
  .contact-name {
    font-family: "Roboto Condensed", sans-serif; font-weight: 700; font-size: 19px; margin-left: 10px;
  }
  .contact-list { list-style: none; margin-top: 4px; }
  .contact-list li { display: flex; align-items: center; gap: 8px; font-size: 13px; margin-top: 7px; }
  .contact-list svg { width: 16px; height: 16px; flex: none; }
  .legal-note {
    position: absolute; left: 370px; top: 560px; width: 370px; text-align: center;
    font-family: "Roboto", sans-serif; font-size: 11px; line-height: 1.4; color: var(--ink-soft);
  }

  /* right panel */
  .cover-title {
    position: absolute; left: 775px; top: 40px; color: var(--white);
  }
  .cover-title .brand-main {
    display: block; font-family: "Anton", sans-serif; font-size: 64px; line-height: 1; letter-spacing: 2px;
  }
  .cover-title .brand-sub {
    display: block; font-family: "Montserrat", sans-serif; font-weight: 300; font-size: 32px;
    letter-spacing: 3px; margin-top: 4px; margin-left: 40px;
  }
  .cover-footer {
    position: absolute; right: 36px; bottom: 48px; color: var(--white);
    font-family: "Roboto Condensed", sans-serif; font-size: 24px; letter-spacing: 0.5px;
  }
</style>
</head>
<body>
<main class="brochure">
  <svg class="brochure-art" viewBox="0 0 1110 760" width="1110" height="760">
    <defs>
      <linearGradient id="gymTone" x1="0" y1="0" x2="1" y2="1">
        <stop offset="0" stop-color="#c9a46a"/>
        <stop offset="0.6" stop-color="#e8cf9e"/>
        <stop offset="1" stop-color="#f4e7cc"/>
      </linearGradient>
      <linearGradient id="skyTone" x1="0" y1="0" x2="0" y2="1">
        <stop offset="0" stop-color="#123f86"/>
        <stop offset="1" stop-color="#2a7fd0"/>
      </linearGradient>
      <linearGradient id="playerTone" x1="0" y1="0" x2="0" y2="1">
        <stop offset="0" stop-color="#dfe5ee"/>
        <stop offset="1" stop-color="#c9d3e2"/>
      </linearGradient>
    </defs>

    <!-- top banner photo across left and middle panels -->
    <rect class="gym-photo" x="0" y="0" width="740" height="300" fill="url(#gymTone)" role="img" aria-label="Photo of girls playing indoor volleyball at the net"/>
    <path d="M0,290 C200,250 450,190 740,110 L740,760 L0,760Z" fill="var(--blue)"/>
    <path d="M0,300 C200,262 450,202 740,124 L740,760 L0,760Z" fill="var(--blue-mid)"/>
    <path d="M0,312 C200,276 450,214 740,138 L740,760 L0,760Z" fill="var(--panel)"/>

    <!-- cover photo -->
    <rect class="cover-photo" x="740" y="0" width="370" height="760" fill="url(#skyTone)" role="img" aria-label="Photo of a girl jumping to hit a beach volleyball over the net against a blue sky"/>

    <!-- left panel player photo -->
    <rect class="player-photo" x="120" y="548" width="180" height="150" rx="6" fill="url(#playerTone)" role="img" aria-label="Photo of a smiling girl in a blue jersey ready to pass a volleyball"/>

    <!-- bottom waves -->
    <path d="M0,650 C250,640 500,620 740,560 C900,520 1000,500 1110,470 L1110,760 L0,760Z" fill="var(--blue-light)"/>
    <path d="M0,666 C250,656 500,638 740,580 C900,542 1000,522 1110,492 L1110,760 L0,760Z" fill="var(--blue-mid)"/>
    <path d="M0,682 C250,672 500,656 740,600 C900,564 1000,544 1110,514 L1110,760 L0,760Z" fill="var(--blue)"/>
    <path d="M0,700 C250,690 500,676 740,622 C900,588 1000,568 1110,540 L1110,760 L0,760Z" fill="var(--navy)"/>
  </svg>

  <section class="info-copy">
    <p>Applications and awards are kept confidential by the fund unless recipients and their parent or guardian consents to disclosure of their name for marketing purposes.</p>
    <p>Please consider contributing to the fund and help make volleyball an accessible sport for young players. Unfortunately, donations are not tax deductible, but they are incredibly valuable and very much appreciated.</p>
  </section>

  <p class="payment-note">Makes checks payable to <span class="payee">NetStar Inc.</span></p>
  <div class="contact-pill">CONTACT US</div>
  <section class="contact-card">
    <p class="contact-name">Margaret Clevin ( President )</p>
    <ul class="contact-list">
      <li>
        <svg viewBox="0 0 16 16" aria-hidden="true"><circle cx="8" cy="8" r="8" fill="var(--blue)"/><path d="M8 3.5a3 3 0 0 0-3 3c0 2.3 3 5.8 3 5.8s3-3.5 3-5.8a3 3 0 0 0-3-3z" fill="#fff"/><circle cx="8" cy="6.5" r="1.1" fill="var(--blue)"/></svg>
        <span>4120 Harbor Lane Fairview, KS 66000</span>
      </li>
      <li>
        <svg viewBox="0 0 16 16" aria-hidden="true"><circle cx="8" cy="8" r="8" fill="var(--blue)"/><path d="M5 4.2l1.6-.4 1 2.2-1 .8a6 6 0 0 0 2.6 2.6l.8-1 2.2 1-.4 1.6c-3.6.2-7-3.2-6.8-6.8z" fill="#fff"/></svg>
        <span>555-847-1926</span>
      </li>
      <li>
        <svg viewBox="0 0 16 16" aria-hidden="true"><circle cx="8" cy="8" r="8" fill="var(--blue)"/><rect x="4" y="5" width="8" height="6" rx="1" fill="#fff"/><path d="M4.3 5.4L8 8.3l3.7-2.9" stroke="var(--blue)" stroke-width="1" fill="none"/></svg>
        <span>netstartrust@mailbox-example.net</span>
      </li>
    </ul>
  </section>
  <p class="legal-note">NetStarInc d/b/a NetStar Trust<br>a Kansas Corporation EI #55-0192837</p>

  <h1 class="cover-title">
    <span class="brand-main">NETSTAR</span>
    <span class="brand-sub">TRUST</span>
  </h1>
  <p class="cover-footer">NETSTAR INC</p>
</main>
</body>
</html>
```